Großartige Zusammenarbeit. Schnell und absolut zuverlässig. Tolle eigene Idee eingebracht. Trelgrafik hat sich sehr mit dem Projekt beschäftigt und hat den Kern perfekt umgesetzt - besser geht nicht!
Zielgruppe
Wir sind der Lindmoorer Kai Verein. Ein Verein der sich für die Neugestaltung des historischen Hafens in Hamburg-Bergedorf stark macht und Projekte auch in die Tat umsetzt für Bergedorf. Finanziert werden wir durch unsere Mitglieder. Unsere Zielgruppe sind Bergedorfer - Privatleute / Firmen / Einzelhandel in Bergedorf. Menschen die Stolz auf Bergedorf sind und ein Teil dieses Prozessen sein möchten und aktiv Ideen haben, wie man das Hafenareal attraktiver gestalten kann.
Aufgabenstellung
Das Plakat-Projekt, welches es umzusetzen gilt, ist eine Veranstaltung die jährlich stattfindet in dem Kolmwik-Hafen. Der Kolmwik ist der Name des Gewässers. 2017 hat sie bereits stattgefunden. Wir brauchen mehr öffentliche Aufmerksamkeit, wollen hiermit potentielle Mitglieder ansprechen. Das Plakat wird z. B. in dem Markt Galerie Lindmoor aushängen, eventuell auch als digitale Werbung auf den Monitoren im Center geschaltet werden.
Zur Veranstaltung: Es gibt 4 Abende, jeweils spielt eine Live-Band (Rock / Blues / etc.) auf dem Deck eines Bootes der Lindmoorer Fährgesellschaft Musik. Vom Anleger aus verfolgen die Gäste das Event und Getränke gibt es auf dem Boot. Es ist ein Open Air Event. Bilder vom letzten Jahr gibt es auf der Webseite www.lindmoorer-kai.de/Aktuelles
Titel: Klang am Lindmoorer Kai
Text: Unter freiem Himmel als Schwimmbühne im Kolmwik. Bei Schlechtwetter in der Tonkeller im Wendthof
Zusatz: Live und umsonst / Bierverkauf vom Schiff
Textänderungen / weitere Vorschläge sind herzlich willkommen, Hauptsache es gibt einen Bezug zum Hafen und zu Bergedorf.
Hochformat: A2 und Flyer Format z.B. A6 / Übliche digitale Formate JPG / EPS / AI... und MP4 (1080x1920 Pixel 72 DPI)
Inhaltstext zu den Bands die spielen werden:
28.06.2018 / 19 Uhr Velvet Hornets (Blues Rock)
26.07.2018 / 19 Uhr Rusty Pistons ( Rock´n Roll)
30.08.2018 / 19 Uhr The Moorland Pipers ( Schottischer Highland Beat)
27.09.2018 / 19 Uhr Korvidan (Deutscher Rock)

```html
<!DOCTYPE html>
<html lang="de">
<head>
<meta charset="utf-8">
<title>Der Hafen rockt – Music on Kolmwik</title>
<link href="https://fonts.googleapis.com/css2?family=Raleway:wght@300;800&family=Amatic+SC:wght@700&family=Righteous&family=Baloo+2:wght@700&family=Open+Sans:wght@400&display=swap" rel="stylesheet">
<style>
  :root {
    --ink: #1f1f1f;
    --orange: #f7ad3e;
    --white: #ffffff;
    --sky-top: #9fb2bb;
    --sky-mid: #d9e1e4;
    --water: #5d7482;
    --water-deep: #2c3b45;
    --logo-blue: #2c3a8c;
  }
  * { margin: 0; padding: 0; box-sizing: border-box; }
  html, body { width: 843px; height: 1200px; overflow: hidden; background: var(--white); }
  .poster {
    position: relative;
    width: 843px;
    height: 1200px;
    overflow: hidden;
  }
  .backdrop {
    position: absolute; inset: 0;
    background:
      radial-gradient(ellipse 420px 260px at 420px 470px, rgba(255,255,255,.65), transparent 70%),
      radial-gradient(ellipse 300px 180px at 320px 760px, rgba(255,255,255,.5), transparent 70%),
      linear-gradient(180deg, var(--sky-top) 0%, #c4d0d5 30%, var(--sky-mid) 45%, #b9c6cc 60%, var(--water) 75%, var(--water-deep) 100%);
  }
  .keyboard {
    position: absolute; left: 0; right: 0; top: 805px; bottom: 0;
    background: linear-gradient(180deg, rgba(255,255,255,0) 0%, rgba(245,245,245,.85) 35%, #e9ecee 100%);
  }
  .headline {
    position: absolute; top: 64px; left: 0; width: 100%;
    text-align: center; color: var(--ink);
    font-family: "Raleway", sans-serif;
  }
  .headline__main { font-weight: 800; font-size: 39px; letter-spacing: 1px; line-height: 44px; }
  .headline__sub { font-weight: 300; font-size: 31px; line-height: 34px; letter-spacing: .5px; }
  .title {
    position: absolute; left: 150px; top: 180px; width: 520px;
    font-family: "Amatic SC", sans-serif; font-weight: 700;
    line-height: 1;
  }
  .title__word { display: flex; align-items: flex-end; height: 210px; }
  .title__word span { display: inline-block; }
  .l-m { color: var(--white); font-size: 210px; transform: rotate(-3deg); }
  .l-u { color: var(--orange); font-size: 190px; margin-top: 40px; }
  .l-s { color: var(--orange); font-size: 205px; }
  .l-i { color: var(--white); font-size: 200px; }
  .l-c { color: var(--orange); font-size: 205px; }
  .title__place {
    position: absolute; left: 268px; top: 190px;
    color: var(--orange); font-size: 58px; letter-spacing: 2px; white-space: nowrap;
  }
  .event {
    position: absolute; width: 340px; text-align: center;
    font-family: "Righteous", sans-serif; color: var(--ink);
  }
  .event__date { font-size: 24px; line-height: 32px; letter-spacing: 1px; }
  .event__band { font-size: 23px; line-height: 34px; }
  .event__genre { font-family: "Baloo 2", sans-serif; font-weight: 700; font-size: 16px; line-height: 22px; color: var(--orange); }
  .event--1 { left: 81px; top: 497px; }
  .event--2 { left: 81px; top: 614px; }
  .event--3 { left: 433px; top: 502px; }
  .event--4 { left: 433px; top: 627px; }
  .weather-note {
    position: absolute; left: 806px; top: 677px;
    transform: rotate(-90deg); transform-origin: 0 0;
    font-family: "Open Sans", sans-serif; font-size: 12.5px; color: var(--ink);
    white-space: nowrap;
  }
  .club {
    position: absolute; left: 32px; top: 978px; width: 275px; height: 111px;
    background: var(--white);
    display: flex; align-items: center; justify-content: center; gap: 10px;
  }
  .club__mark { width: 14px; height: 14px; background: var(--logo-blue); }
  .club__name {
    font-family: "Raleway", sans-serif; font-weight: 800; font-size: 20px;
    color: var(--logo-blue);
  }
</style>
</head>
<body>
<main class="poster">
  <div class="backdrop" role="img" aria-label="Foto: Himmel und glitzernde Wasseroberfläche im Hafen"></div>
  <div class="keyboard" role="img" aria-label="Grafik: Klaviertastatur mit aufsteigenden weißen Balken"></div>

  <header class="headline">
    <h1 class="headline__main">DER HAFEN ROCKT</h1>
    <p class="headline__sub">LIVE UND UMSONST</p>
  </header>

  <div class="title">
    <div class="title__word" aria-label="Music">
      <span class="l-m">M</span><span class="l-u">U</span><span class="l-s">S</span><span class="l-i">I</span><span class="l-c">C</span>
    </div>
    <div class="title__place">ON KOLMWIK</div>
  </div>

  <section class="event event--1">
    <p class="event__date">28.06.2018</p>
    <p class="event__band">19 Uhr Velvet Hornets</p>
    <p class="event__genre">(Blues Rock)</p>
  </section>
  <section class="event event--2">
    <p class="event__date">26.07.2018</p>
    <p class="event__band">19 Uhr Rusty Pistons</p>
    <p class="event__genre">(Rock´n Roll)</p>
  </section>
  <section class="event event--3">
    <p class="event__date">30.08.2018</p>
    <p class="event__band">19 Uhr The Moorland Pipers</p>
    <p class="event__genre">(Schottischer Highland Beat)</p>
  </section>
  <section class="event event--4">
    <p class="event__date">27.09.2018</p>
    <p class="event__band">19 Uhr Korvidan</p>
    <p class="event__genre">(Deutscher Rock)</p>
  </section>

  <p class="weather-note">Bei Schlechtwetter finden die Konzerte im Tonkeller im Wendthof statt.</p>

  <div class="club">
    <span class="club__mark"></span>
    <span class="club__name">Lindmoorer Kai Verein</span>
  </div>
</main>
</body>
</html>
```